Vireno Subscription Infographic

I need an infographic to promote my new subscription service.
The infographic should be clear and consise, showcasing the benefits and the value of my offering.
I have provided a PDF that describes the service, and the offering in detail. I would like the designer to read the pdf document, understand the offering and design a one page infographic that will condense the information in a nice, visual way, to be shared within Workvine for advertisment purposes.

```html
<!DOCTYPE html>
<html lang="en">
<head>
<meta charset="utf-8">
<title>Vireno Technology Subscription</title>
<link href="https://fonts.googleapis.com/css2?family=Roboto:ital,wght@0,400;0,500;0,700;0,900;1,700;1,900&display=swap" rel="stylesheet">
<style>
:root{
  --navy:#12296b;
  --navy-deep:#0b1c4f;
  --wave-light:#5b74a6;
  --title-blue:#0d3a6e;
  --accent-blue:#102f80;
  --ink:#111111;
  --body-ink:#1c1c1c;
  --white:#ffffff;
}
*{margin:0;padding:0;box-sizing:border-box}
html,body{width:1200px;height:675px;overflow:hidden}
body{font-family:"Roboto",Arial,sans-serif;color:var(--body-ink);position:relative;background:#eceef2}
.backdrop{position:absolute;inset:0;background:radial-gradient(ellipse at 20% 30%,#ffffff 0%,#f0f1f4 40%,transparent 70%),linear-gradient(100deg,#f6f6f8 0%,#e6e7eb 45%,#d9d4d2 70%,#e4e5e9 100%)}
.corner-band{position:absolute;left:0;top:0}
.title{position:absolute;left:77px;top:34px;font-style:italic;font-weight:900;font-size:40px;letter-spacing:.3px;color:var(--title-blue);line-height:1}
.subtitle{position:absolute;left:87px;top:85px;font-style:italic;font-weight:900;font-size:33px;color:var(--ink);line-height:1;text-shadow:1px 1px 2px rgba(0,0,0,.2)}
.brand{position:absolute;left:1071px;top:21px;width:129px;height:50px;background:var(--navy);display:flex;align-items:center;gap:6px;padding-left:8px}
.brand-dot{width:22px;height:22px;border-radius:50%;border:3px solid var(--white);flex:none}
.brand-name{color:var(--white);font-weight:700;font-size:13px;line-height:1.05}

.card{position:absolute;background:var(--white);border-radius:8px;overflow:hidden;display:flex;flex-direction:column;align-items:center;text-align:center;box-shadow:0 2px 8px rgba(0,0,0,.18)}
.card-head{position:absolute;left:0;right:0;top:0;height:125px;background:var(--navy);color:var(--white)}
.card-head .wave{position:absolute;left:0;bottom:0;width:100%;height:48px}
.tier{position:absolute;left:0;right:0;font-weight:700;font-size:14px;letter-spacing:.3px}
.price{position:absolute;left:0;right:0;font-weight:700;font-size:26px;line-height:1}
.price .cur{font-size:11px;vertical-align:top;margin-right:8px;position:relative;top:-2px}
.price .per{font-size:6.5px;font-weight:500;margin-left:5px}
.hours{position:absolute;left:0;right:0;font-weight:500;font-size:8.5px;z-index:2}
.card-body{position:relative;display:flex;flex-direction:column;align-items:center;width:100%;height:100%}
.fte{font-weight:700;font-size:12.5px;color:var(--ink);line-height:16px}
.pitch{font-weight:700;font-size:13.5px;line-height:16px;color:var(--accent-blue);margin-top:6px}
.rule{width:62%;height:1px;background:var(--accent-blue);opacity:.75;margin:6px 0}
.group h4{font-weight:700;font-size:10px;line-height:11.5px;color:var(--ink)}
.group p{font-size:8.8px;line-height:10.5px}
.rate{margin-top:auto;margin-bottom:10px;font-weight:700;font-size:20px;color:var(--ink);line-height:1}
.rate .cur{font-size:10px;vertical-align:top}
.rate .per{font-size:7px;font-weight:500;color:#8a8a8a;margin-left:4px}

.starter{left:88px;top:198px;width:169px;height:328px}
.entry{left:264px;top:171px;width:168px;height:382px}
.member{left:439px;top:145px;width:166px;height:420px;border-radius:8px 0 0 8px}
.exclusive{left:598px;top:114px;width:201px;height:497px;z-index:3;box-shadow:0 4px 14px rgba(0,0,0,.3)}
.exclusive .card-head{background:var(--navy-deep)}
.premium{left:799px;top:132px;width:166px;height:463px;z-index:2}

.team{position:absolute;left:1019px;top:165px;width:158px;height:434px;background:var(--white);border-radius:8px;overflow:hidden;box-shadow:0 2px 8px rgba(0,0,0,.18)}
.team-title{position:absolute;left:0;right:0;top:15px;text-align:center;font-weight:700;font-size:14.5px;line-height:17px;color:var(--ink)}
.team-swoosh{position:absolute;left:0;top:54px;width:100%;height:30px}
.role{position:absolute;right:34px;text-align:right;font-weight:700;font-size:8.6px;line-height:10.5px;color:var(--ink)}
.role::after{content:"";position:absolute;right:0;bottom:-6px;width:42px;height:1px;background:var(--accent-blue)}
.role-dot{position:absolute;left:131px;width:15px;height:15px;border-radius:50%;background:var(--navy-deep);border:3px solid #e6e8ee;box-shadow:1px 1px 3px rgba(0,0,0,.3)}
.team-foot{position:absolute;left:0;right:0;bottom:0;height:120px}
.team-foot svg{position:absolute;left:0;top:0;width:100%;height:100%}
.team-foot p{position:absolute;left:0;right:0;top:26px;text-align:center;color:var(--white);font-style:italic;font-weight:700;font-size:11.5px;line-height:13.6px}

.footnote{position:absolute;left:97px;top:589px;font-size:6px;color:var(--ink)}
.terms-title{position:absolute;left:98px;top:603px;font-size:9.5px;font-weight:700;color:var(--ink)}
.terms{position:absolute;left:110px;top:620px;font-size:7px;line-height:9.8px;color:var(--ink);list-style:none}
.base-band{position:absolute;left:0;top:659px;width:692px;height:16px;background:var(--navy);border-radius:0 16px 0 0}
</style>
</head>
<body>
<div class="backdrop" role="img" aria-label="Soft blurred photo of an engineer working at a laptop"></div>

<svg class="corner-band" width="72" height="80" viewBox="0 0 72 80"><polygon points="0,27 40,27 71,79 0,79" fill="#12296b"/></svg>
<h1 class="title">Vireno Technology</h1>
<h2 class="subtitle">SUBSCRIPTION</h2>
<div class="brand"><span class="brand-dot"></span><span class="brand-name">Vireno<br>Technology</span></div>

<!-- Starter -->
<div class="card starter">
  <div class="card-head">
    <div class="tier" style="top:10px">STARTER</div>
    <div class="price" style="top:38px"><span class="cur">£</span>9,280<span class="per">/month</span></div>
    <div class="hours" style="top:80px">160 Hour</div>
    <svg class="wave" viewBox="0 0 200 50" preserveAspectRatio="none"><path d="M0 22 C60 6 120 26 200 14 L200 32 C140 36 70 16 0 32Z" fill="#5b74a6"/><path d="M0 30 C70 16 140 36 200 30 L200 50 L0 50Z" fill="#fff"/><path d="M0 28 C60 22 90 42 130 40 C160 38 180 28 200 30 L200 37 C175 35 160 49 125 48 C85 47 55 31 0 35Z" fill="#12296b"/></svg>
  </div>
  <div class="card-body" style="padding-top:141px">
    <div class="fte">1 FTE</div>
    <div class="pitch">Online Support<br>Only</div>
    <div class="rule"></div>
    <div class="group"><h4>Mainstream Tools</h4><p>Emails<br>Accounts<br>Deskline Office<br>Taskflo</p></div>
    <div class="rule"></div>
    <div class="rate"><span class="cur">£ </span>58<span class="per">/Hourly</span></div>
  </div>
</div>

<!-- Entry -->
<div class="card entry">
  <div class="card-head">
    <div class="tier" style="top:10px">ENTRY</div>
    <div class="price" style="top:37px"><span class="cur">£</span>17,120<span class="per">/month</span></div>
    <div class="hours" style="top:79px">320 Hour</div>
    <svg class="wave" viewBox="0 0 200 50" preserveAspectRatio="none"><path d="M0 22 C60 6 120 26 200 14 L200 32 C140 36 70 16 0 32Z" fill="#5b74a6"/><path d="M0 30 C70 16 140 36 200 30 L200 50 L0 50Z" fill="#fff"/><path d="M0 28 C60 22 90 42 130 40 C160 38 180 28 200 30 L200 37 C175 35 160 49 125 48 C85 47 55 31 0 35Z" fill="#12296b"/></svg>
  </div>
  <div class="card-body" style="padding-top:131px">
    <div class="fte">2 FTE</div>
    <div class="pitch">1 Engineer Semi-<br>pernamenently on Site</div>
    <div class="rule"></div>
    <div class="group"><h4>Mainstream Tools</h4><p>Emails<br>Accounts<br>Deskline Office<br>Taskflo</p></div>
    <div class="rule"></div>
    <div class="group"><h4>Engineering Tools</h4><p>Reliantix<br>Vireno In house<br>Calculators</p></div>
    <div class="rule"></div>
    <div class="rate"><span class="cur">£</span>53.5<span class="per">/Hourly</span></div>
  </div>
</div>

<!-- Member -->
<div class="card member">
  <div class="card-head">
    <div class="tier" style="top:10px;padding-right:6px">MEMBER</div>
    <div class="price" style="top:36px"><span class="cur">£</span>24,900<span class="per">/month</span></div>
    <div class="hours" style="top:79px;padding-right:8px">480 Hour</div>
    <svg class="wave" viewBox="0 0 200 50" preserveAspectRatio="none"><path d="M0 22 C60 6 120 26 200 14 L200 32 C140 36 70 16 0 32Z" fill="#5b74a6"/><path d="M0 30 C70 16 140 36 200 30 L200 50 L0 50Z" fill="#fff"/><path d="M0 28 C60 22 90 42 130 40 C160 38 180 28 200 30 L200 37 C175 35 160 49 125 48 C85 47 55 31 0 35Z" fill="#12296b"/></svg>
  </div>
  <div class="card-body" style="padding-top:128px;padding-right:8px">
    <div class="fte">3 FTE</div>
    <div class="pitch">1 Engineer Semi-<br>pernamenently on Site</div>
    <div class="rule"></div>
    <div class="group"><h4>Mainstream Tools</h4><p>Emails<br>Accounts<br>Deskline Office<br>Taskflo</p></div>
    <div class="rule"></div>
    <div class="group"><h4>Engineering Tools</h4><p>Reliantix<br>Vireno In house<br>Calculators</p></div>
    <div class="rule"></div>
    <div class="group"><h4>Specialist &nbsp;Tools</h4><p>Matrixa<br>Simlinea</p></div>
    <div class="rule"></div>
    <div class="rate"><span class="cur">£</span>51.9<span class="per">/Hourly</span></div>
  </div>
</div>

<!-- Exclusive -->
<div class="card exclusive">
  <div class="card-head">
    <div class="tier" style="top:10px">EXCLUSIVE</div>
    <div class="price" style="top:35px"><span class="cur">£</span>39,600<span class="per">/month</span></div>
    <div class="hours" style="top:79px;padding-right:6px">800 Hour</div>
    <svg class="wave" viewBox="0 0 200 50" preserveAspectRatio="none"><path d="M0 22 C60 6 120 26 200 14 L200 32 C140 36 70 16 0 32Z" fill="#5b74a6"/><path d="M0 30 C70 16 140 36 200 30 L200 50 L0 50Z" fill="#fff"/><path d="M0 28 C60 22 90 42 130 40 C160 38 180 28 200 30 L200 37 C175 35 160 49 125 48 C85 47 55 31 0 35Z" fill="#0b1c4f"/></svg>
  </div>
  <div class="card-body" style="padding-top:131px">
    <div class="fte">5 FTE</div>
    <div class="pitch" style="margin-top:5px">1 Engineers on site<br>1 Engineer Semi-permanently</div>
    <div class="rule"></div>
    <div class="group"><h4>Mainstream Tools</h4><p>Emails<br>Accounts<br>Deskline Office<br>Taskflo</p></div>
    <div class="rule"></div>
    <div class="group"><h4>Engineering Tools</h4><p>Reliantix<br>Vireno In house<br>Calculators</p></div>
    <div class="rule"></div>
    <div class="group"><h4>Specialist &nbsp;Tools</h4><p>Matrixa<br>Simlinea</p></div>
    <div class="rule"></div>
    <div class="group"><h4>High End Software</h4><p>MotoDraft<br>Anvero (Mech)</p></div>
    <div class="rule"></div>
    <div class="group"><h4>Specialist Software</h4><p>Rotaxa<br>Multibody<br>Dynamics</p></div>
    <div class="rule"></div>
    <div class="rate"><span class="cur">£</span>49.5<span class="per">/Hourly</span></div>
  </div>
</div>

<!-- Premium -->
<div class="card premium">
  <div class="card-head">
    <div class="tier" style="top:10px">PREMIUM</div>
    <div class="price" style="top:36px"><span class="cur">£</span>33,000<span class="per">/month</span></div>
    <div class="hours" style="top:79px">640 Hour</div>
    <svg class="wave" viewBox="0 0 200 50" preserveAspectRatio="none"><path d="M0 22 C60 6 120 26 200 14 L200 32 C140 36 70 16 0 32Z" fill="#5b74a6"/><path d="M0 30 C70 16 140 36 200 30 L200 50 L0 50Z" fill="#fff"/><path d="M0 28 C60 22 90 42 130 40 C160 38 180 28 200 30 L200 37 C175 35 160 49 125 48 C85 47 55 31 0 35Z" fill="#12296b"/></svg>
  </div>
  <div class="card-body" style="padding-top:129px">
    <div class="fte">4 FTE</div>
    <div class="pitch" style="font-size:12px;line-height:14px;margin-top:7px">1 Engineers on site<br>1 Engineer Semi-permanently</div>
    <div class="rule"></div>
    <div class="group"><h4>Mainstream Tools</h4><p>Emails<br>Accounts<br>Deskline Office<br>Taskflo</p></div>
    <div class="rule"></div>
    <div class="group"><h4>Engineering Tools</h4><p>Reliantix<br>Vireno In house<br>Calculators</p></div>
    <div class="rule"></div>
    <div class="group"><h4>Specialist Tools</h4><p>Matrixa<br>Simlinea</p></div>
    <div class="rule"></div>
    <div class="group"><h4>High End Software</h4><p>MotoDraft<br>Anvero (Mech)</p></div>
    <div class="rule"></div>
    <div class="rate"><span class="cur">£ </span>50<span class="per">/Hourly</span></div>
  </div>
</div>

<!-- Team leadership -->
<div class="team">
  <div class="team-title">TEAM<br>LEADERSHIP</div>
  <svg class="team-swoosh" viewBox="0 0 160 30" preserveAspectRatio="none"><path d="M0 8 C40 -2 70 22 100 18 C125 15 145 6 160 8 L160 14 C140 12 125 28 95 27 C60 26 35 10 0 14Z" fill="#0b1c4f"/></svg>
  <div class="role" style="top:94px">Electric Motor Design<br>Expert</div><span class="role-dot" style="top:97px"></span>
  <div class="role" style="top:124px">Requirements Engineer<br>(Based In Kestral)</div><span class="role-dot" style="top:128px"></span>
  <div class="role" style="top:164px">Requirements Engineer</div><span class="role-dot" style="top:161px"></span>
  <div class="role" style="top:188px">System Safety And<br>DFMEA Expert</div><span class="role-dot" style="top:192px"></span>
  <div class="role" style="top:220px">Power Electronics And<br>Control Engineer</div><span class="role-dot" style="top:224px"></span>
  <div class="role" style="top:254px">Test And Validation<br>Energy</div><span class="role-dot" style="top:256px"></span>
  <div class="role" style="top:292px">Mechanical Energy</div><span class="role-dot" style="top:288px"></span>
  <div class="team-foot">
    <svg viewBox="0 0 158 120" preserveAspectRatio="none"><path d="M0 10 C40 -4 100 20 158 0 L158 120 L0 120Z" fill="#12296b"/></svg>
    <p>Task Allocation<br>And Deliverable<br>Agreement Based<br>On The Level Of<br>The Subscription<br>Service</p>
  </div>
</div>

<p class="footnote">*FTF = Full Time Equivalent</p>
<p class="terms-title">Additional Terms :</p>
<ol class="terms">
  <li>1) Subscription Level can be adjusted on a 3 month notice (higher/lower number of FTE hours)</li>
  <li>2) If project needs increase, upgrades on the service can be delivered potentially earlier, pending Vireno engineering team availability.</li>
  <li>3) If project needs are reduced, with a 3 month notice we can reallocate the resources to other customers, effectively being able to reduce the subscription service levels</li>
</ol>
<div class="base-band"></div>
</body>
</html>
```